Business cards for modern animal non-profit organization
Vastrel Foundation
Business cards for modern animal non-profit organization - Animals
Creative Brief
Professional
Mirabel T. Ashgrove
President, Founder
no address
mirabel@vastrel.org
www.vastrel.org
501(c)3 non-profit # 84-6159203
Name of organization: Vastrel Foundation Would like to add the phrase: 'Caring for gentle giants and the families who share their land.' Perhaps a split look, the quote on the left, info on the right.
I have a photo I would like to use on the back side with the logo.
mirabel mirabel
Site Admin, Fairly sure I uploaded the .ai file of my logo. Please let me know if I need to do anything else.
tidewarp tidewarp
Forgot to mention. Please no cartoon elephants. Not needed. Please check out my website to see the our style. www.vastrel.org I do not like the font you see for 'vastrel' in blue on the website. Please do not use that. I prefer the elegant look of the font on my logo. Thanks

```html
<!DOCTYPE html>
<html lang="en">
<head>
<meta charset="utf-8">
<title>Vastrel Foundation — Business Cards</title>
<link href="https://fonts.googleapis.com/css2?family=Questrial&family=Open+Sans:wght@300;400;600&display=swap" rel="stylesheet">
<style>
  :root {
    --canvas: #e6e6e4;
    --card-white: #ffffff;
    --brand-blue: #2ea3d8;
    --ink-gray: #6f7377;
    --ink-dark: #4a4d50;
    --mark-gray: #5d6063;
    --photo-dark: #3b3530;
    --photo-mid: #7a6f64;
    --photo-light: #a89d90;
    --panel: rgba(70, 84, 96, 0.78);
  }
  * { margin: 0; padding: 0; box-sizing: border-box; }
  html, body { width: 1200px; height: 901px; overflow: hidden; }
  body {
    background: var(--canvas);
    font-family: "Open Sans", Arial, sans-serif;
    position: relative;
  }
  .card {
    position: absolute;
    left: 300px;
    width: 600px;
    height: 343px;
    border-radius: 14px;
    overflow: hidden;
    box-shadow: 0 6px 18px rgba(0,0,0,0.18);
  }
  .card--front { top: 77px; background: var(--card-white); }
  .card--back { top: 480px; }

  /* front */
  .brand {
    position: absolute;
    left: 44px;
    top: 90px;
    display: flex;
    align-items: center;
    gap: 12px;
  }
  .brand__dot {
    width: 40px; height: 40px;
    border-radius: 50%;
    background: var(--mark-gray);
  }
  .brand__name {
    font-family: "Questrial", sans-serif;
    font-size: 38px;
    color: var(--brand-blue);
    letter-spacing: 1px;
  }
  .tagline {
    position: absolute;
    left: 44px;
    top: 168px;
    width: 250px;
    font-size: 11px;
    line-height: 15px;
    color: var(--ink-gray);
    text-transform: uppercase;
    letter-spacing: 0.3px;
  }
  .tagline__mark {
    font-family: Georgia, serif;
    font-size: 26px;
    line-height: 0;
    color: var(--brand-blue);
    font-weight: bold;
    vertical-align: -8px;
  }
  .tagline__mark--open { margin-right: 4px; }
  .tagline__mark--close { margin-left: 3px; }
  .contact {
    position: absolute;
    left: 330px;
    top: 110px;
    right: 0;
  }
  .contact__name {
    font-size: 19px;
    font-weight: 300;
    color: var(--ink-dark);
    padding-bottom: 6px;
  }
  .contact__rule {
    height: 2px;
    background: var(--brand-blue);
    margin-bottom: 26px;
  }
  .contact__item {
    display: flex;
    align-items: center;
    gap: 8px;
    font-size: 11px;
    color: var(--ink-gray);
    margin-bottom: 8px;
  }
  .contact__item svg { width: 12px; height: 12px; flex: none; }

  /* back */
  .photo {
    position: absolute; inset: 0;
    background:
      radial-gradient(ellipse at 30% 45%, var(--photo-light) 0%, var(--photo-mid) 40%, var(--photo-dark) 100%);
  }
  .panel {
    position: absolute;
    left: 330px;
    top: 40px;
    width: 240px;
    height: 250px;
    background: var(--panel);
    display: flex;
    flex-direction: column;
    align-items: center;
    justify-content: flex-end;
  }
  .panel__brand {
    display: flex;
    flex-direction: column;
    align-items: center;
    gap: 12px;
    margin-bottom: 34px;
  }
  .panel__dot {
    width: 48px; height: 48px;
    border-radius: 50%;
    background: var(--card-white);
  }
  .panel__name {
    font-family: "Questrial", sans-serif;
    font-size: 30px;
    color: var(--card-white);
    letter-spacing: 1px;
  }
  .panel__band {
    width: 100%;
    background: var(--brand-blue);
    color: var(--card-white);
    font-size: 7.5px;
    line-height: 11px;
    text-transform: uppercase;
    text-align: center;
    padding: 8px 10px;
    letter-spacing: 0.3px;
  }
</style>
</head>
<body>

<section class="card card--front" aria-label="Business card front">
  <div class="brand">
    <span class="brand__dot"></span>
    <span class="brand__name">VASTREL</span>
  </div>
  <p class="tagline"><span class="tagline__mark tagline__mark--open">&ldquo;</span>Caring for gentle giants and the families who share their land<span class="tagline__mark tagline__mark--close">&rdquo;</span></p>
  <div class="contact">
    <p class="contact__name">Mirabel T. Ashgrove</p>
    <div class="contact__rule"></div>
    <p class="contact__item">
      <svg viewBox="0 0 12 12"><rect x="0.5" y="2" width="11" height="8" rx="1" fill="none" stroke="var(--brand-blue)"/><path d="M0.5 2.5 L6 6.5 L11.5 2.5" fill="none" stroke="var(--brand-blue)"/></svg>
      mirabel@vastrel.org
    </p>
    <p class="contact__item">
      <svg viewBox="0 0 12 12"><circle cx="6" cy="6" r="5.5" fill="none" stroke="var(--brand-blue)"/><ellipse cx="6" cy="6" rx="2.4" ry="5.5" fill="none" stroke="var(--brand-blue)"/><path d="M0.5 6 H11.5" stroke="var(--brand-blue)"/></svg>
      www.vastrel.org
    </p>
  </div>
</section>

<section class="card card--back" aria-label="Business card back">
  <div class="photo" role="img" aria-label="Close-up photograph of an elephant's wrinkled skin and eye"></div>
  <div class="panel">
    <div class="panel__brand">
      <span class="panel__dot"></span>
      <span class="panel__name">VASTREL</span>
    </div>
    <p class="panel__band">Caring for gentle giants and the families who share their land</p>
  </div>
</section>

</body>
</html>
```